Velk Method Body Wash & Shampoo

Label design for an Activated charcoal body wash and shampoo for first responders after fires. Product removes soot and smoke smell. Deep cleansing. Red and black tones in label. Product is deep black and bottle transparent. Label is wrapped around bottle and can be with transparent or coloured background. Bottle diameter is 19cm and height is 17cm.

Target Market(s)

Product will be used by Firefighters, first responders, outdoor/nature active and grill enthusiasts.

Industry/Entity Type

Health and hygiene

Colors
EB3D1F
EC4F4E
F09395
F8D3D4
FCEDEE

Requirements
Must have
• Serious design. Design that fits for 250 and 500ml bottles. Place for ingredients and contact info at the back of the bottle..
Nice to have
• Attractive clean design, attached logo. Logo can be on front or back. "medical" or health associations would be good.
Should not have
• Multi color, pictures. Playfulness.

```html
<!DOCTYPE html>
<html lang="en">
<head>
<meta charset="utf-8">
<title>Velk Method Body Wash &amp; Shampoo Label</title>
<link rel="stylesheet" href="https://fonts.googleapis.com/css2?family=Antonio:wght@300;400&family=Bodoni+Moda:wght@400;500;600&display=swap">
<style>
  :root {
    --label-bg: #fcedee;
    --ink: #111111;
    --accent-red: #c8141c;
    --accent-red-light: #eb3d1f;
  }
  * { margin: 0; padding: 0; box-sizing: border-box; }
  html, body {
    width: 1200px;
    height: 1000px;
    overflow: hidden;
    background: var(--label-bg);
  }
  .label {
    width: 1200px;
    height: 1000px;
    display: flex;
    flex-direction: column;
    align-items: center;
    text-align: center;
    font-family: "Bodoni Moda", serif;
    color: var(--ink);
    padding-top: 82px;
  }
  .claim-title {
    color: var(--accent-red);
    font-size: 22px;
    font-weight: 500;
    letter-spacing: 0.2em;
  }
  .claim-sub {
    color: var(--accent-red);
    font-size: 14px;
    letter-spacing: 0.18em;
    margin-top: 18px;
  }
  .product-kind {
    font-size: 34px;
    letter-spacing: 0.2em;
    margin-top: 64px;
  }
  .product-name {
    font-family: "Antonio", sans-serif;
    font-weight: 300;
    font-size: 118px;
    line-height: 1.02;
    letter-spacing: 0.05em;
    margin-top: 18px;
  }
  .brand-mark {
    display: flex;
    align-items: center;
    gap: 14px;
    margin-top: 46px;
  }
  .brand-dot {
    width: 26px;
    height: 26px;
    border-radius: 50%;
    background: var(--accent-red);
  }
  .brand-name {
    font-size: 40px;
    font-weight: 600;
    color: var(--accent-red);
    letter-spacing: 0.04em;
  }
  .approval-label {
    font-family: "Antonio", sans-serif;
    font-weight: 400;
    font-size: 13px;
    color: var(--accent-red);
    margin-top: 42px;
    letter-spacing: 0.04em;
  }
  .partner-badge {
    width: 58px;
    height: 58px;
    margin-top: 12px;
    border-radius: 50%;
    background: var(--accent-red-light);
  }
  .used-by {
    font-size: 15px;
    font-weight: 500;
    letter-spacing: 0.2em;
    margin-top: 38px;
  }
  .audience {
    font-size: 15px;
    line-height: 1.75;
    letter-spacing: 0.18em;
    margin-top: 26px;
  }
  .volume {
    font-size: 19px;
    font-weight: 500;
    letter-spacing: 0.2em;
    margin-top: 38px;
  }
</style>
</head>
<body>
  <main class="label">
    <p class="claim-title">DEEP CLEASING</p>
    <p class="claim-sub">PRODUCT REMOVES SOOT AND SMOKE SMELL</p>
    <p class="product-kind">ACTIVATED CHARCOAL</p>
    <h1 class="product-name">BODY WASH<br>&amp; SHAMPOO</h1>
    <div class="brand-mark">
      <span class="brand-dot"></span>
      <span class="brand-name">Velk Method</span>
    </div>
    <p class="approval-label">APPROVED BY:</p>
    <div class="partner-badge" role="img" aria-label="Partner approval badge"></div>
    <p class="used-by">USED BY:</p>
    <p class="audience">FIREFIGHTERS / FIRST RESPONDERS / OUTDOOR<br>NATURE ACTIVE AND GRILL ENTHUSIASTS</p>
    <p class="volume">500 ML</p>
  </main>
</body>
</html>
```